The Verdant Ledger App - Modernization & Graphics User Interface Friendliness Updates

We are Verdant Ledger, and we want to bring a new branding look and graphical user interface to the Verdant Ledger App. The app is a quick reference encyclopedia for all things produce. Boasting articles on over 2,000 produce items, with information ranging from taste and application to geographical and cultural significance. Included in its features are over 10 thousand recipes, and the Verdant Ledger App Harvest Circle – a global initiative to connect farmer, customer, and chef in one sustainable and easy to use application. The design needs to bring a greater sense of social connection – encouraging the user to participate in the 'Harvest Circled' experience voluntarily. The design should reflect a sense of authority reflecting the authenticity and reliability of the provided information, it's writing, and its sources. Download the App here: vledgr.example/install

Target Market(s)

Women and Men between ages 21-55.

Industry/Entity Type

Education

Font styles to use
Serif
Sans Serif

Colors

Designer to choose colors to be used in the design.

Requirements
Must have
• An updated user interface, the intuitive usability of the app is currently non-existent. We are looking to reflect as the authority on produce. The app design must reflect a professional, user-friendly, up-to-date, and trustworthy feel.
Nice to have
• To incorporate the social draw of the Harvest Circle we would like to include on the home page "Social Bubbles" (think Pictoloop stories) which updates with shared photos of produce and their location.
Should not have
• An overly complicated theme, distracting or unprofessional colors, and images.

```html
<!DOCTYPE html>
<html lang="en">
<head>
<meta charset="utf-8">
<title>Verdant Ledger – Explore</title>
<link rel="stylesheet" href="https://fonts.googleapis.com/css2?family=Inter:wght@400;500;700;800&display=swap">
<style>
:root{
  --brand-green:#24891d;
  --bubble-ring:#3a9a2c;
  --ink:#111111;
  --muted:#8a8a8a;
  --backdrop:#e4e8f0;
  --white:#ffffff;
  --divider:#e3e3e3;
  --tabbar:#2b2624;
  --tab-inactive:#5e5855;
}
*{box-sizing:border-box;margin:0;padding:0}
html,body{width:800px;height:1200px;overflow:hidden}
body{background:var(--backdrop);font-family:"Inter",sans-serif;color:var(--ink);position:relative}
.board-header{position:absolute;left:0;top:0;width:800px;height:64px;background:var(--white)}
.board-title{position:absolute;left:18px;top:20px;font-size:24px;font-weight:800;letter-spacing:-0.3px}
.board-count{position:absolute;right:18px;top:24px;font-size:18px;font-weight:400;color:#333}
.screen{position:absolute;left:149px;top:103px;width:502px;height:1045px;background:var(--white);overflow:hidden}
.app-bar{position:absolute;left:0;top:0;width:100%;height:86px;background:var(--brand-green);color:var(--white)}
.status{position:absolute;top:6px;left:0;width:100%;height:18px;font-size:15px}
.status .carrier{position:absolute;left:9px;top:0;display:flex;align-items:center;gap:5px}
.status .clock{position:absolute;left:0;width:100%;text-align:center}
.status .battery{position:absolute;right:8px;top:0;display:flex;align-items:center;gap:5px}
.app-title{position:absolute;left:0;width:100%;top:42px;text-align:center;font-size:22px;font-weight:800;letter-spacing:0.5px}
.search-icon{position:absolute;right:22px;top:43px}
.section-title{position:absolute;left:16px;font-size:27px;font-weight:800;letter-spacing:-0.4px}
.see-all{position:absolute;right:18px;font-size:20px;color:var(--brand-green)}
.divider{position:absolute;left:0;width:100%;height:1px;background:var(--divider)}
.bubble{position:absolute;top:158px;width:101px;height:101px;border-radius:50%;border:2px solid var(--bubble-ring);padding:3px}
.bubble .photo{width:100%;height:100%;border-radius:50%}
.bubble-label{position:absolute;top:269px;width:130px;text-align:center;font-size:17px;line-height:20px}
.post{position:absolute;top:407px;width:201px}
.post .photo{width:201px;height:134px;border-radius:3px}
.post-text{margin-top:13px;font-size:21px;line-height:28px;white-space:nowrap}
.post-time{margin-top:4px;font-size:19px;color:var(--muted)}
.spot{position:absolute;top:766px;width:134px;text-align:center}
.spot .photo{width:134px;height:133px;border-radius:3px}
.spot-name{margin-top:12px;font-size:17px;white-space:nowrap}
.spot-date{margin-top:2px;font-size:17px;color:var(--muted)}
.tab-bar{position:absolute;left:0;top:979px;width:100%;height:66px;background:var(--tabbar);display:flex}
.tab{flex:1;display:flex;flex-direction:column;align-items:center;padding-top:12px;font-size:12px;color:var(--tab-inactive)}
.tab svg{margin-bottom:4px}
.tab.is-active{color:var(--white)}
</style>
</head>
<body>
<header class="board-header">
  <div class="board-title">Verdant Ledger</div>
  <div class="board-count">8 Screens</div>
</header>

<main class="screen">
  <div class="app-bar">
    <div class="status">
      <span class="carrier">●●●○○ Carrier
        <svg width="16" height="12" viewBox="0 0 16 12"><path d="M1 4a10 10 0 0 1 14 0M3.5 6.5a6.5 6.5 0 0 1 9 0M6 9a3 3 0 0 1 4 0" stroke="#fff" stroke-width="1.6" fill="none"/></svg></span>
      <span class="clock">3:24 PM</span>
      <span class="battery">100%
        <svg width="34" height="14" viewBox="0 0 34 14"><rect x="0.5" y="0.5" width="30" height="13" rx="2.5" fill="none" stroke="#fff"/><rect x="2.5" y="2.5" width="26" height="9" rx="1" fill="#fff"/><rect x="31.5" y="4.5" width="2" height="5" fill="#fff"/></svg></span>
    </div>
    <div class="app-title">EXPLORE</div>
    <svg class="search-icon" width="26" height="26" viewBox="0 0 26 26"><circle cx="11" cy="11" r="8.5" fill="none" stroke="#fff" stroke-width="2.6"/><line x1="17.5" y1="17.5" x2="24" y2="24" stroke="#fff" stroke-width="2.8" stroke-linecap="round"/></svg>
  </div>

  <h2 class="section-title" style="top:108px">Social Bubbles</h2>
  <span class="see-all" style="top:114px">See all</span>
  <div class="bubble" style="left:16px"><div class="photo" role="img" aria-label="Layered autumn salad in a glass" style="background:radial-gradient(circle,#5a2a22,#c9c2bf 70%)"></div></div>
  <div class="bubble" style="left:147px"><div class="photo" role="img" aria-label="Hand holding an ice cream cone" style="background:radial-gradient(circle,#a0714d,#2f3a2c 70%)"></div></div>
  <div class="bubble" style="left:276px"><div class="photo" role="img" aria-label="Cup of creamy baobab drink" style="background:radial-gradient(circle,#d8c6ae,#4a3b32 75%)"></div></div>
  <div class="bubble" style="left:407px"><div class="photo" role="img" aria-label="Trays of durian egg tarts" style="background:radial-gradient(circle,#e3b58a,#8a5a44 75%)"></div></div>
  <div class="bubble-label" style="left:1px">Autumn<br>Salad</div>
  <div class="bubble-label" style="left:132px">Ambrosia<br>Mojito</div>
  <div class="bubble-label" style="left:261px">Baobab<br>Juice</div>
  <div class="bubble-label" style="left:392px">Durian<br>Egg Tarts</div>
  <div class="divider" style="top:333px"></div>

  <h2 class="section-title" style="top:357px">#VerdantLedger</h2>
  <span class="see-all" style="top:363px">See all</span>
  <article class="post" style="left:16px">
    <div class="photo" role="img" aria-label="Burger buns and sliced vegetables on a board" style="background:linear-gradient(135deg,#6b5a48,#c4a27c 50%,#4d7a35)"></div>
    <p class="post-text">Ocean view dining<br>with a delectable<br>menu. &nbsp;#verdantl...</p>
    <p class="post-time">4h ago</p>
  </article>
  <article class="post" style="left:233px">
    <div class="photo" role="img" aria-label="Almond cookies on a red plate" style="background:linear-gradient(135deg,#b0574d,#c98a6b 55%,#a4524a)"></div>
    <p class="post-text">Special I got going<br>on tonight and<br>tomorrow here at...</p>
    <p class="post-time">5h ago</p>
  </article>
  <article class="post" style="left:450px">
    <div class="photo" role="img" aria-label="Green leafy produce" style="background:linear-gradient(90deg,#9fb49a,#4f7548)"></div>
    <p class="post-text">#Repost<br>@fieldhand<br>we're</p>
    <p class="post-time">8h ago</p>
  </article>
  <div class="divider" style="top:692px"></div>

  <h2 class="section-title" style="top:716px">Recently Spotted</h2>
  <span class="see-all" style="top:722px">See all</span>
  <div class="spot" style="left:16px">
    <div class="photo" role="img" aria-label="Green Mutsu apples" style="background:radial-gradient(circle at 40% 50%,#d7df7e,#9bb43f 70%)"></div>
    <div class="spot-name">Apple Mutsu</div><div class="spot-date">4h ago</div>
  </div>
  <div class="spot" style="left:166px">
    <div class="photo" role="img" aria-label="Ripe peaches" style="background:radial-gradient(circle at 45% 50%,#f0a96a,#c64a32 75%)"></div>
    <div class="spot-name">Peaches</div><div class="spot-date">Yesterday</div>
  </div>
  <div class="spot" style="left:316px">
    <div class="photo" role="img" aria-label="Opened durian fruit" style="background:radial-gradient(circle at 55% 45%,#efe49a,#5e6a2e 65%)"></div>
    <div class="spot-name">Durian</div><div class="spot-date">9/9/17</div>
  </div>
  <div class="spot" style="left:466px">
    <div class="photo" role="img" aria-label="Orange squash" style="background:linear-gradient(135deg,#e4581e,#b8401a)"></div>
    <div class="spot-name">Squash</div><div class="spot-date">&nbsp;</div>
  </div>

  <nav class="tab-bar">
    <div class="tab is-active">
      <svg width="26" height="26" viewBox="0 0 26 26"><circle cx="13" cy="13" r="12" fill="#fff"/><path d="M18 8l-3 7-7 3 3-7z" fill="none" stroke="#2b2624" stroke-width="1.8"/><circle cx="13" cy="13" r="1.3" fill="#2b2624"/></svg>Explore</div>
    <div class="tab">
      <svg width="26" height="26" viewBox="0 0 26 26"><path d="M13 8c-3-2-8-1-8 5s4 11 8 9c4 2 8-3 8-9s-5-7-8-5z" fill="none" stroke="#5e5855" stroke-width="1.6"/><path d="M13 8c0-3 1-5 3-6" fill="none" stroke="#5e5855" stroke-width="1.6"/></svg>Produce</div>
    <div class="tab">
      <svg width="26" height="26" viewBox="0 0 26 26"><path d="M13 3a6 6 0 0 1 6 6c0 5-6 10-6 10S7 14 7 9a6 6 0 0 1 6-6z" fill="none" stroke="#5e5855" stroke-width="1.6"/><circle cx="13" cy="9" r="2.2" fill="none" stroke="#5e5855" stroke-width="1.6"/><path d="M8 19l-5 5h20l-5-5" fill="none" stroke="#5e5855" stroke-width="1.6"/></svg>Spotted</div>
    <div class="tab">
      <svg width="26" height="26" viewBox="0 0 26 26"><rect x="5" y="3" width="16" height="21" fill="none" stroke="#5e5855" stroke-width="1.6"/><path d="M9 10h8M9 14h8M9 18h8M9 1v4M13 1v4M17 1v4" stroke="#5e5855" stroke-width="1.6"/></svg>Recipes</div>
    <div class="tab">
      <svg width="26" height="26" viewBox="0 0 26 26"><circle cx="13" cy="13" r="12" fill="none" stroke="#5e5855" stroke-width="1.6"/><circle cx="8" cy="13" r="1.4" fill="#5e5855"/><circle cx="13" cy="13" r="1.4" fill="#5e5855"/><circle cx="18" cy="13" r="1.4" fill="#5e5855"/></svg>More</div>
  </nav>
</main>
</body>
</html>
```